Flyer-Design für Vermittlung von Immobilien
Zielgruppe
Immobilien vermitteln, für Käufer und Verkäufer, für Mieter und Vermieter
Aufgabenstellung
Inhalt Seite 1: Wir verkaufen Ihr Grundstück, Ihr Haus, Ihre Wohnung
Inhalt Seite 2: Wir suchen für solvente Kunden Ihr Grundstück, Ihr Haus, Ihre Wohnung
Weiterhin soll das Design in Anlehnung der DOLKAN Visitenkarte (siehe vorhergehendes Projekt) layoutet werden. Die Kontakte sollen explizit auf einen Makler mit Foto verweisen.

```html
<!DOCTYPE html>
<html lang="de">
<head>
<meta charset="utf-8">
<title>DOLKAN Immobilien – Flyer</title>
<link href="https://fonts.googleapis.com/css2?family=Overpass:wght@400;700;800;900&display=swap" rel="stylesheet">
<style>
  :root {
    --navy: #14264a;
    --navy-light: #34466a;
    --ink: #13234a;
    --white: #ffffff;
    --page: #ffffff;
    --photo-street-a: #8fa6b8;
    --photo-street-b: #6f9a4a;
    --photo-meeting-a: #6b5a4a;
    --photo-meeting-b: #c9c2b8;
    --portrait-a: #d8d4cf;
    --portrait-b: #8d8a88;
  }
  * { box-sizing: border-box; margin: 0; padding: 0; }
  html, body { width: 1200px; height: 1118px; overflow: hidden; background: var(--page); }
  body { position: relative; font-family: "Overpass", Arial, sans-serif; color: var(--ink); }

  .flyer {
    position: absolute;
    width: 501px; height: 1000px;
    overflow: hidden;
    background: linear-gradient(160deg, var(--navy-light) 0%, var(--navy) 35%, var(--navy) 100%);
    box-shadow: 0 6px 28px rgba(0,0,0,.22);
  }
  .flyer--sell { left: 65px; top: 66px; }
  .flyer--agent { left: 646px; top: 64px; }

  .photo { position: absolute; left: 0; top: 0; width: 100%; }
  .photo--street { height: 614px; background: linear-gradient(180deg, var(--photo-street-a) 0%, #b9c3c4 40%, var(--photo-street-b) 75%, #9aa58a 100%); }
  .photo--meeting { height: 336px; background: linear-gradient(120deg, var(--photo-meeting-a) 0%, var(--photo-meeting-b) 55%, #8a7a6a 100%); }

  .bubble {
    position: absolute;
    background: var(--white);
    text-align: center;
    box-shadow: 0 2px 8px rgba(0,0,0,.18);
    color: var(--ink);
  }
  .bubble__tail { position: absolute; overflow: visible; }
  .bubble__title { font-weight: 900; font-size: 33px; line-height: 38px; letter-spacing: .2px; }
  .bubble__sub { font-weight: 800; font-size: 20px; line-height: 27px; }

  .bubble--search { left: 41px; top: 31px; width: 351px; height: 173px; padding-top: 18px; }
  .bubble--search .bubble__sub { margin-top: 8px; }
  .bubble--sale { left: 111px; top: 409px; width: 351px; height: 146px; padding-top: 22px; }
  .bubble--sale .bubble__sub { margin-top: 8px; }
  .bubble--partner { left: 76px; top: 290px; width: 353px; height: 119px; padding-top: 18px; }
  .bubble--partner .bubble__sub { font-size: 20px; line-height: 27px; }

  .callout-band {
    position: absolute; left: 0; top: 614px; width: 100%; height: 54px;
    background: var(--white);
    text-align: center; font-size: 20px; line-height: 54px; color: var(--ink);
  }
  .callout-band strong { font-weight: 800; }

  .brand {
    position: absolute; left: 0; width: 100%;
    display: flex; align-items: center; justify-content: center; gap: 16px;
    color: var(--white);
  }
  .brand__mark { width: 22px; height: 22px; background: var(--white); }
  .brand__name { font-weight: 800; font-size: 40px; letter-spacing: 12px; line-height: 1; padding-top: 6px; }
  .flyer--sell .brand { top: 788px; }
  .flyer--agent .brand { top: 850px; }

  .contact { position: absolute; left: 0; width: 100%; text-align: center; color: var(--white); font-weight: 700; font-size: 17px; line-height: 21px; }
  .flyer--sell .contact { top: 900px; }
  .contact__web { margin-top: 5px; }
  .flyer--agent .contact--web { top: 944px; }

  .agent { position: absolute; left: 0; top: 434px; width: 100%; text-align: center; color: var(--white); }
  .agent__portrait {
    display: block; margin: 0 auto; width: 116px; height: 154px;
    border: 2px solid #e6e6e6;
    background: linear-gradient(180deg, var(--portrait-a) 0%, var(--portrait-b) 100%);
  }
  .agent__name { margin-top: 24px; font-weight: 800; font-size: 17px; line-height: 20px; }
  .agent__role { font-size: 17px; line-height: 22px; font-weight: 400; }
  .agent__contact { margin-top: 18px; font-weight: 700; font-size: 17px; line-height: 21px; }
</style>
</head>
<body>

<section class="flyer flyer--sell">
  <div class="photo photo--street" role="img" aria-label="Foto: moderne Wohnhäuser mit Bäumen, Hecken und Blumen an einem sonnigen Gehweg"></div>

  <div class="bubble bubble--search">
    <svg class="bubble__tail" style="left:26px;top:172px" width="60" height="44"><polygon points="0,0 58,0 58,42" fill="#fff"/></svg>
    <h2 class="bubble__title">Wir suchen für<br>solvente Kunden</h2>
    <p class="bubble__sub">Ihr Grundstück, Ihr Haus,<br>Ihre Wohnung!</p>
  </div>

  <div class="bubble bubble--sale">
    <svg class="bubble__tail" style="left:270px;top:145px" width="50" height="44"><polygon points="0,0 50,0 0,42" fill="#fff"/></svg>
    <h2 class="bubble__title">Wir verkaufen</h2>
    <p class="bubble__sub">Ihr Grundstück, Ihr Haus,<br>Ihre Wohnung!</p>
  </div>

  <p class="callout-band"><strong>Rufen Sie uns an!</strong> Wir beraten Sie gerne.</p>

  <div class="brand"><span class="brand__mark"></span><span class="brand__name">DOLKAN</span></div>

  <div class="contact">
    <p>+49 (0) 170 4 52 81 36</p>
    <p>l.brandt@dolkan.immo</p>
    <p class="contact__web">www.dolkan.immo</p>
  </div>
</section>

<section class="flyer flyer--agent">
  <div class="photo photo--meeting" role="img" aria-label="Foto: zwei Personen besiegeln mit Handschlag einen Immobilienkauf"></div>

  <div class="bubble bubble--partner">
    <svg class="bubble__tail" style="left:270px;top:118px" width="52" height="44"><polygon points="0,0 50,0 0,42" fill="#fff"/></svg>
    <p class="bubble__sub">Wir sind Ihr kompetenter<br>Partner im Bereich Kauf und<br>Verkauf von Immobilien.</p>
  </div>

  <div class="agent">
    <span class="agent__portrait" role="img" aria-label="Porträtfoto der Maklerin"></span>
    <p class="agent__name">Lena Brandt</p>
    <p class="agent__role">Meister(in) / Immobilienberatung</p>
    <div class="agent__contact">
      <p>+49 (0) 170 4 52 81 36</p>
      <p>l.brandt@dolkan.immo</p>
    </div>
  </div>

  <div class="brand"><span class="brand__mark"></span><span class="brand__name">DOLKAN</span></div>

  <p class="contact contact--web">www.dolkan.immo</p>
</section>

</body>
</html>
```